Walk Boldly into Morning: 48 Days to a Year of Courage and Calm

This is a non-fiction, self-help book. The first edition was published a decade ago, and it needs a new design. Nothing too literal (no actual hearts on the cover) but something inspirational or perhaps something quite plain. The current cover is below for reference, but I DO NOT want something similar to that. It is outdated.

The cover must include:

1. Title: Walk Boldly into Morning
2. Subtitle: 48 Days to a Year of Courage and Calm
3. Author Name: Dean Forsythe

It should also have plenty of "white space" in other words the fonts shouldnt be so big that they take up the whole cover.

Dimensions: 9" x 6.25"

Target Market(s)

adults interested in personal development

Font styles to use
Serif
Script

Colors

Designer to choose colors to be used in the design.

Requirements
Must have
• Classic look and feel. The current design is too busy. I have included examples of the style I like below. I'm open to a singular graphic/photo but nothing more than that. Probably plain text is best.
• Please look at the samples I have included of best-selling books in the genre that I like. The cover should be modeled after these.

```html
<!DOCTYPE html>
<html lang="en">
<head>
<meta charset="utf-8">
<title>Walk Boldly into Morning — Dean Forsythe</title>
<link rel="stylesheet" href="https://fonts.googleapis.com/css2?family=Cormorant+Garamond:ital,wght@0,400;0,500;1,400&family=Pinyon+Script&display=swap">
<style>
  :root {
    --backdrop: #000000;
    --paper: #fdfbf6;
    --ink: #1f2a44;
    --ink-soft: #4a5570;
    --gold: #b8893a;
  }
  html, body {
    margin: 0;
    padding: 0;
    width: 933px;
    height: 1200px;
    overflow: hidden;
    background: var(--backdrop);
  }
  /* 6.25 × 9 in trim: 522 × 752 px */
  .book-cover {
    position: absolute;
    left: 205px;
    top: 224px;
    width: 522px;
    height: 752px;
    box-sizing: border-box;
    padding: 78px 56px 70px;
    background: var(--paper);
    display: flex;
    flex-direction: column;
    align-items: center;
    text-align: center;
    font-family: "Cormorant Garamond", Garamond, serif;
    color: var(--ink);
  }
  .author {
    margin: 0;
    font-size: 17px;
    font-weight: 500;
    letter-spacing: 0.3em;
    text-transform: uppercase;
    color: var(--ink-soft);
  }
  .spacer-top { flex: 1; }
  .spacer-bottom { flex: 1.35; }
  .title {
    margin: 0;
    font-weight: 400;
    display: flex;
    flex-direction: column;
    align-items: center;
  }
  .title-line {
    display: block;
    font-size: 60px;
    line-height: 1.05;
    letter-spacing: 0.01em;
  }
  .title-script {
    display: block;
    font-family: "Pinyon Script", cursive;
    font-size: 50px;
    line-height: 1.1;
    color: var(--gold);
    margin: 4px 0 6px;
  }
  .title-last {
    font-size: 66px;
  }
  .divider {
    width: 54px;
    height: 1px;
    background: var(--gold);
    margin: 36px 0 30px;
    border: 0;
  }
  .subtitle {
    margin: 0;
    font-style: italic;
    font-size: 21px;
    line-height: 1.45;
    color: var(--ink-soft);
  }
</style>
</head>
<body>
  <main class="book-cover">
    <p class="author">Dean Forsythe</p>
    <div class="spacer-top"></div>
    <h1 class="title">
      <span class="title-line">Walk Boldly</span>
      <span class="title-script">into</span>
      <span class="title-line title-last">Morning</span>
    </h1>
    <hr class="divider">
    <p class="subtitle">48 Days to a Year<br>of Courage and Calm</p>
    <div class="spacer-bottom"></div>
  </main>
</body>
</html>
```